Brivora Australia Company Values.

We have just completed our company purpose, beliefs and values (for the first time, we have not had these before)
We are now wanting to add images to each company value as a visual
so they are easily identified and understood for all our staff - we need them to remember the 5 Values.
We are a manufacturer of dental materials and infection control products, based in Melbourne.

What we would like:
- A Poster (that can be placed in our staff lunch rooms)
- The values to be lined up Horizontally
- Image on the top of the words
- Wording does not all need to be the same text font
- No image photographs - please use image graphics
- No images with people
- No dental related graphics

Target audience: Brivora staff

Our Values are:
Think Big
Have a go, learn and adapt
If you're gonna do it, do it bloody well
Empower Others
Be a good human

I have uploaded some examples.

Target Market(s)

Brivora Team members

Industry/Entity Type

Healthcare

Colors

Designer to choose colors to be used in the design.

Requirements
Must have
• Clear horizontal layout, space between each value
Should not have
• No images with humans or dental

```html
<!DOCTYPE html>
<html lang="en">
<head>
<meta charset="utf-8">
<title>Brivora Australia – Our Values</title>
<link rel="stylesheet" href="https://fonts.googleapis.com/css2?family=Montserrat:wght@700&family=Raleway:wght@700&display=swap">
<style>
  :root {
    --page-bg: #e9eef0;
    --poster-bg-top: #ffffff;
    --poster-bg-bottom: #eef5fb;
    --red: #e30613;
    --ink: #1b1b1b;
    --ink-light: #ffffff;
    --think-fill: #7ecbdf;
    --think-line: #6fc6d6;
    --learn-fill: #b6dfd5;
    --learn-line: #4fb49a;
    --quality-fill: #3f1b5e;
    --quality-line: #3b1a5a;
    --empower-fill: #f7ef8f;
    --empower-line: #e8df5a;
    --human-fill: #cce0aa;
    --human-line: #8fb062;
  }
  * { margin: 0; padding: 0; box-sizing: border-box; }
  html, body {
    width: 1200px; height: 1000px; overflow: hidden;
    background: var(--page-bg);
  }
  .poster {
    position: absolute; left: 290px; top: 82px;
    width: 584px; height: 826px; overflow: hidden;
    background: linear-gradient(160deg, var(--poster-bg-top) 40%, var(--poster-bg-bottom));
  }
  .poster-title {
    position: absolute; left: 0; width: 100%; top: 26px;
    text-align: center;
    font-family: "Montserrat", sans-serif; font-weight: 700;
    font-size: 48px; letter-spacing: -1px; color: var(--red);
  }
  .hex-art { position: absolute; left: 0; top: 0; }
  .value-icon {
    position: absolute; border-radius: 14px;
    transform: translate(-50%, -50%);
  }
  .icon-think   { left: 171px; top: 238px; width: 92px; height: 96px;
                  background: linear-gradient(90deg, #f4b53f, #2ba3b6); }
  .icon-learn   { left: 409px; top: 240px; width: 92px; height: 80px;
                  background: linear-gradient(135deg, #f7c35a, #f5eee4 45%, #f07d7d); }
  .icon-quality { left: 275px; top: 434px; width: 80px; height: 82px;
                  background: linear-gradient(135deg, #e4eef2, #8fc3d4); }
  .icon-empower { left: 170px; top: 650px; width: 84px; height: 82px;
                  background: linear-gradient(180deg, #3a6fae, #f4b55c); }
  .icon-human   { left: 405px; top: 642px; width: 96px; height: 80px;
                  background: linear-gradient(90deg, #2d5f9e, #f4c7a4); }
  .value-label {
    position: absolute; width: 190px; text-align: center;
    font-family: "Raleway", sans-serif; font-weight: 700;
    font-size: 18px; line-height: 23.5px; color: var(--ink);
  }
  .value-label.on-dark { color: var(--ink-light); }
</style>
</head>
<body>
<main class="poster">
  <h1 class="poster-title">Our Values</h1>

  <svg class="hex-art" width="584" height="826" viewBox="0 0 584 826" aria-hidden="true">
    <defs>
      <filter id="hex-shadow" x="-20%" y="-20%" width="140%" height="140%">
        <feDropShadow dx="3" dy="5" stdDeviation="5" flood-color="#000" flood-opacity=".18"/>
      </filter>
      <polygon id="hex-frame" points="0,-118 117,-52 117,52 0,118 -117,52 -117,-52"/>
      <polygon id="hex-tile" points="0,-98 97,-42 97,54 0,108 -97,54 -97,-42"/>
    </defs>

    <rect class="title-rule" x="64" y="106" width="455" height="2" fill="var(--red)"/>
    <rect class="title-rule-accent" x="228" y="103" width="127" height="8" fill="var(--red)"/>

    <g class="value-hex think" transform="translate(171 252)">
      <use href="#hex-frame" fill="none" stroke="var(--think-line)" stroke-width="2"/>
      <use href="#hex-tile" fill="var(--think-fill)" filter="url(#hex-shadow)"/>
    </g>
    <g class="value-hex learn" transform="translate(412 252)">
      <use href="#hex-frame" fill="none" stroke="var(--learn-line)" stroke-width="2"/>
      <use href="#hex-tile" fill="var(--learn-fill)" filter="url(#hex-shadow)"/>
    </g>
    <g class="value-hex quality" transform="translate(292 471)">
      <use href="#hex-frame" fill="#fff" stroke="var(--quality-line)" stroke-width="2"/>
      <use href="#hex-tile" fill="var(--quality-fill)" filter="url(#hex-shadow)"/>
    </g>
    <g class="value-hex empower" transform="translate(171 678)">
      <use href="#hex-frame" fill="none" stroke="var(--empower-line)" stroke-width="2"/>
      <use href="#hex-tile" fill="var(--empower-fill)" filter="url(#hex-shadow)"/>
    </g>
    <g class="value-hex human" transform="translate(412 678)">
      <use href="#hex-frame" fill="none" stroke="var(--human-line)" stroke-width="2"/>
      <use href="#hex-tile" fill="var(--human-fill)" filter="url(#hex-shadow)"/>
    </g>
  </svg>

  <div class="value-icon icon-think" role="img" aria-label="Illustration of a light bulb with a brain inside, surrounded by small idea icons"></div>
  <div class="value-icon icon-learn" role="img" aria-label="Illustration of an open book with a small glowing light bulb"></div>
  <div class="value-icon icon-quality" role="img" aria-label="Illustration of a clipboard checklist with a magnifying glass"></div>
  <div class="value-icon icon-empower" role="img" aria-label="Illustration of two open hands holding up a simple figure symbol"></div>
  <div class="value-icon icon-human" role="img" aria-label="Illustration of a thumbs-up with a small notification badge"></div>

  <p class="value-label" style="left:76px; top:299px;">Think Big</p>
  <p class="value-label" style="left:317px; top:299px;">Have a go, learn<br>and adapt</p>
  <p class="value-label on-dark" style="left:197px; top:487px;">If you're gonna<br>do it, do it bloody<br>well</p>
  <p class="value-label" style="left:76px; top:707px;">Empower<br>Others</p>
  <p class="value-label" style="left:317px; top:707px;">Be a good<br>human</p>
</main>
</body>
</html>
```